Revise our price listr for 2023

Please see attached price list with new prices to revise.
Please include new logo
Please add the text: Please note that prices are subject to change without prior notice.
Please remove prices from equipment with operator
Please add Under Commercial stone:
Fill Dirt $16.
Please add under Decorative Stone:
3/4" Barn Red Stone $127.
3/4" Yellow Ocean Gravel $140.
3/4" Delaware River Gravel $110.
1" Nutmeg Pebble $97.
Price list sending via email and customer in our lobby
Landscape and construction supply

```html
<!DOCTYPE html>
<html lang="en">
<head>
<meta charset="utf-8">
<title>Ridgeline Supply – 2023 Material Price List</title>
<link rel="stylesheet" href="https://fonts.googleapis.com/css2?family=Graduate&family=Catamaran:wght@400;500;600;700;800&display=swap">
<style>
  :root{
    --green:#1c9a4a;
    --green-dark:#13773a;
    --maroon:#7a1d24;
    --frame:#6b2a1c;
    --ink:#2b2b2b;
    --paper:#f3f4f5;
    --paper-shade:#e3e6e8;
    --rule:#8a8a8a;
  }
  *{box-sizing:border-box;margin:0;padding:0}
  html,body{width:1200px;height:875px;overflow:hidden}
  body{
    font-family:"Catamaran",sans-serif;color:var(--ink);
    background:radial-gradient(ellipse at 30% 40%,#ffffff 0%,var(--paper) 45%,var(--paper-shade) 100%);
    position:relative;
  }
  .abs{position:absolute}

  /* brand */
  .brand{left:48px;top:70px;display:flex;align-items:center;gap:14px}
  .brand-dot{width:58px;height:58px;border-radius:50%;background:var(--green)}
  .brand-name{font-weight:800;color:var(--maroon);font-size:46px;line-height:.95;letter-spacing:.5px}
  .brand-name small{display:block;font-size:30px;letter-spacing:9px}

  .title-card{left:40px;top:192px;width:323px;height:86px;border:4px solid var(--maroon);
    display:flex;flex-direction:column;align-items:center;justify-content:center;
    font-family:"Graduate",serif;color:var(--green);line-height:1.15;text-align:center;
    -webkit-text-stroke:.6px var(--green)}
  .title-card .year{font-size:21px}
  .title-card .label{font-size:21px}

  /* price boxes */
  .box{border:2px solid var(--frame)}
  .tab{position:absolute;left:50%;transform:translateX(-50%);background:linear-gradient(#25b158,var(--green-dark));
    color:#fff;font-family:"Graduate",serif;border-radius:10px;border:2px solid #fff;
    box-shadow:0 0 0 1px var(--green-dark);text-shadow:1px 1px 1px rgba(0,0,0,.45);
    display:flex;align-items:center;justify-content:center;white-space:nowrap;text-align:center;line-height:1.15}
  .rows{list-style:none}
  .row{display:flex;align-items:baseline;font-size:8.6px;line-height:14.7px}
  .row .item{white-space:nowrap}
  .row .dots{flex:1;border-bottom:1px dashed var(--rule);margin:0 4px;transform:translateY(-3px)}
  .row .price{color:var(--maroon);font-weight:700;width:34px;white-space:nowrap}
  .commercial .row{font-size:9.5px;line-height:14.4px}

  .notice{left:48px;top:828px;width:322px;font-size:9.5px;line-height:12px;font-style:italic;color:var(--maroon);text-align:center}

  /* photo area */
  .photo{left:400px;top:700px;width:402px;height:175px;
    background:linear-gradient(135deg,#b9bec4 0%,#8e949b 40%,#d8d5cf 70%,#9aa0a7 100%);
    -webkit-mask-image:radial-gradient(ellipse 70% 80% at 55% 75%,#000 45%,transparent 100%);
            mask-image:radial-gradient(ellipse 70% 80% at 55% 75%,#000 45%,transparent 100%)}

  /* equipment */
  .equip{left:809px;top:65px;width:356px;height:576px}
  .equip .t{position:absolute;font-size:8.6px;line-height:14.7px;white-space:nowrap}
  .equip .head{font-size:10.5px;font-weight:600}
  .equip .rule{position:absolute;height:2px;background:var(--maroon)}
  .call{color:var(--maroon);font-weight:700}
  .note{position:absolute;left:0;right:0;text-align:center;font-size:12px;line-height:15px;font-weight:500}

  /* did you know */
  .dyk{left:870px;top:665px;width:230px;height:50px}
  .dyk .roll{position:absolute;left:0;top:4px;width:40px;height:44px;border-radius:4px;
    background:linear-gradient(90deg,#8e9399,#f2f3f4 45%,#a4a9ae)}
  .dyk .band{position:absolute;left:36px;top:6px;right:0;height:40px;background:var(--maroon);
    color:#fff;font-family:"Graduate",serif;font-size:18px;display:flex;align-items:center;justify-content:center;
    border-bottom:2px solid var(--green)}
  .facts{left:809px;width:356px;text-align:center;font-size:14px;line-height:1.2}
  .pct{display:inline-block;width:22px;height:22px;border-radius:50%;background:var(--green);color:#fff;
    font-size:13px;font-weight:700;line-height:22px;vertical-align:middle;margin-right:6px}
  .g{color:var(--green);font-weight:600}
  .thanks{color:var(--maroon);font-weight:800;font-size:19px}
</style>
</head>
<body>

  <!-- brand -->
  <div class="abs brand">
    <span class="brand-dot"></span>
    <div class="brand-name">Ridgeline<small>SUPPLY</small></div>
  </div>
  <div class="abs title-card">
    <span class="year">2023</span>
    <span class="label">MATERIAL PRICE LIST</span>
  </div>

  <!-- soil -->
  <section class="abs box" style="left:48px;top:323px;width:321px;height:115px;padding:26px 28px 0 22px">
    <h2 class="tab" style="top:-16px;width:132px;height:33px;font-size:16px">SOIL</h2>
    <ul class="rows">
      <li class="row"><span class="item">Sandy Loam</span><span class="dots"></span><span class="price">$30</span></li>
      <li class="row"><span class="item">Topsoil - Screened</span><span class="dots"></span><span class="price">$42</span></li>
      <li class="row"><span class="item">Garden Soil</span><span class="dots"></span><span class="price">$52</span></li>
      <li class="row"><span class="item">Mushroom Dirt</span><span class="dots"></span><span class="price">$55</span></li>
      <li class="row"><span class="item">Compost (Leaf &amp; Grass)</span><span class="dots"></span><span class="price">$55</span></li>
    </ul>
  </section>

  <!-- mulch -->
  <section class="abs box" style="left:48px;top:479px;width:321px;height:125px;padding:25px 28px 0 22px">
    <h2 class="tab" style="top:-14px;width:144px;height:27px;font-size:16px">MULCH</h2>
    <ul class="rows">
      <li class="row"><span class="item">Mulch-Dyed Black</span><span class="dots"></span><span class="price">$42</span></li>
      <li class="row"><span class="item">Mulch-Dyed Red</span><span class="dots"></span><span class="price">$42</span></li>
      <li class="row"><span class="item">Mulch-Dyed Brown</span><span class="dots"></span><span class="price">$42</span></li>
      <li class="row"><span class="item">Mulch-Natural Light Brown</span><span class="dots"></span><span class="price">$38</span></li>
      <li class="row"><span class="item">Mulch-Natural Triple Ground</span><span class="dots"></span><span class="price">$44</span></li>
      <li class="row"><span class="item">Mulch Cedar</span><span class="dots"></span><span class="price">$55</span></li>
    </ul>
  </section>

  <!-- sand -->
  <section class="abs box" style="left:49px;top:650px;width:321px;height:66px;padding:26px 28px 0 22px">
    <h2 class="tab" style="top:-16px;width:140px;height:29px;font-size:16px">SAND</h2>
    <ul class="rows">
      <li class="row"><span class="item">Masonary / Pool Sand</span><span class="dots"></span><span class="price">$45</span></li>
      <li class="row"><span class="item">Bedding Sand</span><span class="dots"></span><span class="price">$37</span></li>
    </ul>
  </section>

  <!-- seasonal -->
  <section class="abs box" style="left:50px;top:761px;width:320px;height:57px;padding:30px 28px 0 22px">
    <h2 class="tab" style="top:-14px;width:152px;height:27px;font-size:16px">SEASONAL</h2>
    <ul class="rows">
      <li class="row" style="font-size:11px"><span class="item">Treated Salt Green</span><span class="dots" style="margin-left:20px"></span><span class="price">$145</span></li>
    </ul>
  </section>

  <p class="abs notice">Please note that prices are subject to change without prior notice.</p>

  <!-- decorative stone -->
  <section class="abs box" style="left:425px;top:49px;width:356px;height:209px;padding:32px 20px 0 24px">
    <h2 class="tab" style="top:-16px;width:228px;height:32px;font-size:17px">DECORATIVE STONE</h2>
    <ul class="rows">
      <li class="row"><span class="item">White Limestone # 1(1/4" - 1/2")</span><span class="dots"></span><span class="price">$95</span></li>
      <li class="row"><span class="item">White Limestone #2(1/2" - 3/4")</span><span class="dots"></span><span class="price">$97.50</span></li>
      <li class="row"><span class="item">River Rock #2(3/4") Round</span><span class="dots"></span><span class="price">$50</span></li>
      <li class="row"><span class="item">River Rock - Medium (2/3")</span><span class="dots"></span><span class="price">$95</span></li>
      <li class="row"><span class="item">River Rounds (4-6")</span><span class="dots"></span><span class="price">$90</span></li>
      <li class="row"><span class="item">Pea Gravel</span><span class="dots"></span><span class="price">$50</span></li>
      <li class="row"><span class="item">Berkshire Blend</span><span class="dots"></span><span class="price">$120</span></li>
      <li class="row"><span class="item">3/4" Barn Red Stone</span><span class="dots"></span><span class="price">$127</span></li>
      <li class="row"><span class="item">3/4" Yellow Ocean Gravel</span><span class="dots"></span><span class="price">$140</span></li>
      <li class="row"><span class="item">3/4" Delaware River Gravel</span><span class="dots"></span><span class="price">$110</span></li>
      <li class="row"><span class="item">1" Nutmeg Pebble</span><span class="dots"></span><span class="price">$97</span></li>
    </ul>
  </section>

  <!-- commercial stone -->
  <section class="abs box commercial" style="left:425px;top:317px;width:356px;height:182px;padding:28px 20px 0 24px">
    <h2 class="tab" style="top:-17px;width:228px;height:34px;font-size:17px">COMMEACIAL STONE</h2>
    <ul class="rows">
      <li class="row"><span class="item">Item #4</span><span class="dots"></span><span class="price">$42</span></li>
      <li class="row"><span class="item">#1 Stone (1/2")</span><span class="dots"></span><span class="price">$45</span></li>
      <li class="row"><span class="item">#2 Stone (3/4"1")</span><span class="dots"></span><span class="price">$45</span></li>
      <li class="row"><span class="item">#3 (1.5"2")</span><span class="dots"></span><span class="price">$45</span></li>
      <li class="row"><span class="item">Stone Chip (fine)</span><span class="dots"></span><span class="price">$40</span></li>
      <li class="row"><span class="item">Stone Dust (xtra fine)</span><span class="dots"></span><span class="price">$47</span></li>
      <li class="row"><span class="item">Shale When Available</span><span class="dots"></span><span class="price">$Call</span></li>
      <li class="row"><span class="item">Bank Run Fill (Dirt &amp; Cobble)</span><span class="dots"></span><span class="price">$18</span></li>
      <li class="row"><span class="item">Crusher Run</span><span class="dots"></span><span class="price">$42</span></li>
      <li class="row"><span class="item">Fill Dirt</span><span class="dots"></span><span class="price">$16</span></li>
    </ul>
  </section>

  <!-- delivery -->
  <section class="abs box" style="left:425px;top:559px;width:356px;height:145px;padding:38px 20px 0 24px">
    <h2 class="tab" style="top:-18px;width:212px;height:35px;font-size:17px">DELIVERY STONE</h2>
    <ul class="rows">
      <li class="row" style="font-size:9.2px"><span class="item">Local (Small Truck)</span><span class="dots"></span><span class="price">$42</span></li>
      <li class="row" style="font-size:9.2px"><span class="item">Local (Medium Truck)</span><span class="dots"></span><span class="price">$45</span></li>
      <li class="row" style="font-size:9.2px"><span class="item">Local (Large Truck)</span><span class="dots"></span><span class="price">$45</span></li>
    </ul>
    <p style="color:var(--green);font-size:9.5px;text-align:center;margin:8px 0 6px">Local&nbsp; Daliyarius 7 Mile Radius Excluding the mat.</p>
    <ul class="rows">
      <li class="row" style="font-size:9px"><span class="item">Non Local</span><span class="dots"></span><span class="price">CALL</span></li>
    </ul>
    <p style="text-align:right;color:var(--maroon);font-weight:700;font-size:8.6px;line-height:10px;margin-right:-10px">FOR QUOTE</p>
  </section>

  <div class="abs photo" role="img" aria-label="Photo of a gloved hand setting grey paving stones with a rubber mallet and trowel"></div>

  <!-- equipment -->
  <section class="abs box equip">
    <h2 class="tab" style="top:-32px;width:276px;height:62px;font-size:17px">EQUIPMENT WITH<br>OPERATOR AVAILABLE</h2>
    <span class="t" style="left:27px;top:48px">Onsite Mobile</span>
    <span class="t" style="left:27px;top:62px">Grinding/Tub Grinding</span>
    <span class="t" style="left:27px;top:77px">Forestry Mulching</span>
    <span class="t call" style="left:250px;top:49px;font-size:12px">Call For Pricing</span>
    <span class="rule" style="left:54px;top:106px;width:260px"></span>

    <span class="t" style="left:27px;top:118px">Skid Steer: (Rubber Track)</span>
    <span class="t" style="left:27px;top:133px">Available Attachment</span>
    <span class="t" style="left:27px;top:147px">Harley Rake</span>
    <span class="t" style="left:27px;top:162px">Forestry Mulching</span>
    <span class="t" style="left:131px;top:147px">3/4 YArd Buckeet</span>
    <span class="t" style="left:131px;top:162px">Hydraullic Auger</span>
    <span class="t" style="left:131px;top:176px">Grapple Bucket</span>

    <span class="t head" style="left:26px;top:207px">EXCAVATOR:</span>
    <span class="rule" style="left:107px;top:215px;width:222px"></span>
    <span class="t" style="left:27px;top:235px">35 Class (7,500lbs)</span>
    <span class="t" style="left:27px;top:250px">60 Class (14,000lbs)</span>
    <span class="t" style="left:27px;top:264px">140 Class (45,500lbs)</span>
    <span class="t" style="left:27px;top:279px">160 Class (38,500lbs)</span>
    <span class="t" style="left:27px;top:293px">250 Class (60,500lbs)</span>

    <span class="t head" style="left:26px;top:325px">BULL DOZER:</span>
    <span class="rule" style="left:116px;top:333px;width:222px"></span>
    <span class="t" style="left:26px;top:352px">450 Class (18,000lbs)</span>
    <span class="t" style="left:26px;top:367px">700 Class (30,000bs)</span>
    <span class="rule" style="left:53px;top:401px;width:260px"></span>

    <span class="t" style="left:26px;top:421px">Vibratory Roller</span>
    <span class="t" style="left:26px;top:436px">Rock Hammer</span>

    <p class="note" style="top:470px">Hydraulic Rock Hammer on 160 Class excavator.<br>Additional mobilization fee for 1st day $250 day</p>

    <ul class="rows" style="position:absolute;left:26px;right:18px;top:513px">
      <li class="row"><span class="item">Tri-Axle Dump</span><span class="dots"></span><span class="price call" style="width:auto">CALL</span></li>
      <li class="row"><span class="item">Dump Trailer</span><span class="dots"></span><span class="price call" style="width:auto">CALL</span></li>
    </ul>
  </section>

  <!-- did you know -->
  <div class="abs dyk">
    <span class="roll"></span>
    <span class="band">DID YOU KNOW</span>
  </div>
  <p class="abs facts" style="top:737px"><span class="pct">%</span>We Offer Onside Tub grinding</p>
  <p class="abs facts" style="top:770px">We are a <span class="g">GREEN RECYCLING</span> Location</p>
  <p class="abs facts" style="top:796px">NON LOCAL CALL FOR PRICING ALSO</p>
  <p class="abs facts thanks" style="top:824px">THANK YOU</p>

</body>
</html>
```